Business card for a Exhibition booth fabrication company

Hi. My company would like to change our corporate name card. We are an events and Exhibition stand builder company. We would like our corporate name card to resonate what we do. I need someone to create something unique that relates to the industry that I am in. The graphic designer should be creative to incorporate the elements of my industry and try to blend in well in the design of the card. Our aim is to ensure that we are unique and our card can look different from our competitors.
Updates

The decision maker was very busy and didnt had time to make this decision

Target Market(s)

Marketing and events manager from all companies

Contact Information for Business Card

The business card should have the following details:
Name
Job Title
Email
Website

Colors

Designer to choose colors to be used in the design.

Requirements
Must have
• The card must be look something that is relevant to the service that I am providing. My website is: www.velmora-buildworks.example
• You can see my website to get more information on what service that I am doing
Nice to have
• On the back of my card, I would like to have a globe image with the incorporation of my company logo. This is to indicate that my services can be done in any part of the world.

```html
<!DOCTYPE html>
<html lang="en">
<head>
<meta charset="utf-8">
<title>Velmora Buildworks – Business Card</title>
<link href="https://fonts.googleapis.com/css2?family=Montserrat:wght@500;700&family=Open+Sans:wght@400&display=swap" rel="stylesheet">
<style>
  :root {
    --bg: #141414;
    --card: #262626;
    --card-edge: #1f1f1f;
    --map-tone: #343434;
    --red: #e0262b;
    --ink: #e9e9e9;
    --ink-soft: #cfcfcf;
    --rule: #6a6a6a;
  }
  * { margin: 0; padding: 0; box-sizing: border-box; }
  html, body {
    width: 1200px; height: 900px; overflow: hidden;
    background: var(--bg);
  }
  .sheet {
    width: 1200px; height: 900px;
    display: flex; flex-direction: column;
    align-items: center; justify-content: space-evenly;
  }
  .card {
    position: relative;
    width: 700px; height: 400px;
    background: linear-gradient(135deg, #2b2b2b 0%, var(--card) 55%, var(--card-edge) 100%);
    box-shadow: 0 14px 30px rgba(0,0,0,.55);
    overflow: hidden;
  }

  /* front */
  .card-front { display: flex; align-items: center; }
  .brand {
    display: flex; align-items: center; gap: 12px;
    font-family: "Montserrat", sans-serif;
    font-weight: 500;
    color: var(--ink); text-transform: uppercase;
    white-space: nowrap;
  }
  .brand-dot {
    width: 22px; height: 22px; border-radius: 50%;
    background: var(--red); flex: none;
  }
  .card-front .brand-area {
    width: 360px; height: 100%;
    display: flex; align-items: center; justify-content: center;
    padding: 0 28px;
  }
  .card-front .brand { font-size: 15px; letter-spacing: 2.5px; }
  .divider {
    width: 1px; height: 170px; background: var(--rule); flex: none;
  }
  .contact { padding-left: 32px; }
  .contact-name {
    font-family: "Montserrat", sans-serif; font-weight: 700;
    color: var(--red); font-size: 24px; letter-spacing: 1px;
    text-transform: uppercase;
  }
  .contact-title {
    font-family: "Open Sans", sans-serif; color: var(--ink-soft);
    font-size: 14px; margin: 2px 0 16px;
  }
  .contact-list { list-style: none; }
  .contact-list li {
    display: flex; align-items: center; gap: 10px;
    font-family: "Open Sans", sans-serif; color: var(--ink);
    font-size: 14px; line-height: 1.7;
    white-space: nowrap;
  }
  .contact-list svg { width: 12px; height: 12px; flex: none; fill: var(--red); }

  /* back */
  .card-back { display: flex; align-items: center; justify-content: center; }
  .world-map {
    position: absolute; inset: 30px 40px;
    background: radial-gradient(ellipse at 50% 50%, var(--map-tone) 0%, rgba(52,52,52,.45) 55%, transparent 75%);
  }
  .card-back .brand { position: relative; font-size: 24px; letter-spacing: 3px; gap: 14px; }
  .card-back .brand-dot { width: 26px; height: 26px; }
</style>
</head>
<body>
<main class="sheet">
  <section class="card card-front">
    <div class="brand-area">
      <div class="brand"><span class="brand-dot"></span>Velmora Buildworks</div>
    </div>
    <div class="divider"></div>
    <div class="contact">
      <h1 class="contact-name">Adrian Lowe</h1>
      <p class="contact-title">Managing Director</p>
      <ul class="contact-list">
        <li><svg viewBox="0 0 24 24"><path d="M6.6 10.8a15.1 15.1 0 0 0 6.6 6.6l2.2-2.2a1 1 0 0 1 1-.25 11.4 11.4 0 0 0 3.6.6 1 1 0 0 1 1 1V20a1 1 0 0 1-1 1A17 17 0 0 1 3 4a1 1 0 0 1 1-1h3.5a1 1 0 0 1 1 1c0 1.250.2 2.45.6 3.6a1 1 0 0 1-.25 1z"/></svg>+65 8123 4567</li>
        <li><svg viewBox="0 0 24 24"><path d="M2 5h20v14H2z M2 5l10 8 10-8" stroke="#262626" stroke-width="1.5"/></svg>info@velmora-buildworks.example</li>
        <li><svg viewBox="0 0 24 24"><circle cx="12" cy="12" r="10"/><path d="M2 12h20M12 2c3 3 3 17 0 20M12 2c-3 3-3 17 0 20" stroke="#262626" stroke-width="1.5" fill="none"/></svg>www.velmora-buildworks.example</li>
      </ul>
    </div>
  </section>

  <section class="card card-back">
    <div class="world-map" role="img" aria-label="Faint world map spanning the card background"></div>
    <div class="brand"><span class="brand-dot"></span>Velmora Buildworks</div>
  </section>
</main>
</body>
</html>
```